Birchline Septic Solutions

Would like to see some single sided ones but would also like to see some double sided with one sided only being the logo. Owners name is Tom Halvick. Phone number is 555-214-0387
Services are pumping, inspections, installs, and repairs

Contact Information for Business Card

555-241-0387 Tom Halvick Alder Falls, OH

```html
<!DOCTYPE html>
<html lang="en">
<head>
<meta charset="utf-8">
<title>Birchline Septic Solutions – Business Card</title>
<link rel="stylesheet" href="https://fonts.googleapis.com/css2?family=Montserrat:wght@500;600;700;800&display=swap">
<style>
  :root {
    --backdrop: #1b1b1c;
    --card: #111112;
    --teal: #2bbcb6;
    --white: #ffffff;
  }
  * { margin: 0; padding: 0; box-sizing: border-box; }
  html, body { width: 1200px; height: 900px; overflow: hidden; }
  body {
    background: var(--backdrop);
    font-family: "Montserrat", sans-serif;
    display: flex;
    flex-direction: column;
    align-items: center;
    justify-content: center;
    gap: 56px;
  }
  .card {
    position: relative;
    width: 630px;
    height: 360px;
    background: var(--card);
    box-shadow: 0 12px 30px rgba(0,0,0,0.55);
    overflow: hidden;
  }
  .card__band {
    position: absolute;
    left: 0; right: 0; bottom: 0;
    height: 11px;
    background: var(--teal);
  }

  /* Front: name mark */
  .card--front {
    display: flex;
    align-items: center;
    justify-content: center;
  }
  .wordmark {
    display: flex;
    align-items: center;
    gap: 16px;
    margin-top: -20px;
  }
  .wordmark__square {
    width: 22px; height: 22px;
    background: var(--teal);
  }
  .wordmark__text {
    color: var(--white);
    font-weight: 800;
    text-align: center;
    line-height: 1;
  }
  .wordmark__name {
    display: block;
    font-size: 54px;
    letter-spacing: 2px;
  }
  .wordmark__tagline {
    display: block;
    font-size: 17px;
    letter-spacing: 7px;
    margin-top: 10px;
  }

  /* Back: contact */
  .contact {
    position: absolute;
    top: 118px;
    left: 78px;
    display: flex;
    align-items: flex-start;
  }
  .contact__name {
    color: var(--teal);
    font-weight: 700;
    font-size: 27px;
    letter-spacing: 0.5px;
    width: 240px;
    line-height: 1.3;
    padding-top: 4px;
  }
  .contact__divider {
    width: 1px;
    height: 72px;
    background: var(--teal);
    margin: 0 28px 0 12px;
  }
  .contact__list {
    list-style: none;
    padding-top: 14px;
  }
  .contact__item {
    display: flex;
    align-items: center;
    gap: 12px;
    color: var(--white);
    font-weight: 500;
    font-size: 18px;
    letter-spacing: 0.5px;
    margin-bottom: 12px;
  }
  .contact__icon { width: 17px; height: 17px; flex: none; }

  .services {
    position: absolute;
    left: 0; right: 0;
    bottom: 38px;
    text-align: center;
    color: var(--white);
    font-weight: 600;
    font-size: 16.5px;
    letter-spacing: 1px;
  }
  .services__dot {
    display: inline-block;
    width: 8px; height: 8px;
    border-radius: 50%;
    background: var(--teal);
    margin: 0 10px;
    vertical-align: middle;
  }
</style>
</head>
<body>

  <section class="card card--front">
    <div class="wordmark">
      <span class="wordmark__square"></span>
      <div class="wordmark__text">
        <span class="wordmark__name">BIRCHLINE</span>
        <span class="wordmark__tagline">SEPTIC SOLUTIONS</span>
      </div>
    </div>
    <div class="card__band"></div>
  </section>

  <section class="card card--back">
    <div class="contact">
      <h1 class="contact__name">TOM HALVICK</h1>
      <div class="contact__divider"></div>
      <ul class="contact__list">
        <li class="contact__item">
          <svg class="contact__icon" viewBox="0 0 24 24" aria-hidden="true">
            <path fill="#2bbcb6" d="M6.6 10.8a15.1 15.1 0 0 0 6.6 6.6l2.2-2.2c.3-.3.7-.4 1-.2 1.1.4 2.3.6 3.6.6.6 0 1 .4 1 1V20c0 .6-.4 1-1 1A17 17 0 0 1 3 4c0-.6.4-1 1-1h3.5c.6 0 1 .4 1 1 0 1.3.2 2.5.6 3.6.1.3 0 .7-.2 1z"/>
          </svg>
          555-214-0387
        </li>
        <li class="contact__item">
          <svg class="contact__icon" viewBox="0 0 24 24" aria-hidden="true">
            <path fill="#2bbcb6" d="M12 2a7 7 0 0 0-7 7c0 5.2 7 13 7 13s7-7.8 7-13a7 7 0 0 0-7-7zm0 9.5A2.5 2.5 0 1 1 12 6.5a2.5 2.5 0 0 1 0 5z"/>
          </svg>
          Alder Falls, OH
        </li>
      </ul>
    </div>

    <p class="services">
      PUMPING<span class="services__dot"></span>INSPECTIONS<span class="services__dot"></span>INSTALLS<span class="services__dot"></span>REPAIRS
    </p>
    <div class="card__band"></div>
  </section>

</body>
</html>
```